Used Car Dealer seeks an Amazing Business Card Design

We are looking for a business card design that incorporates our logo and grabs the attention of anyone we give the business card to.

Looking to use the same colors as the logo. Our Logo choice is the black background with Red and Silver/Grey Lettering.

We also would like to see some embossed designs.

Target Market(s)

Used Car Buyers, Automotive, Auto

Industry/Entity Type

Automotive

Contact Information for Business Card

BVEL7K
Gordon Whitlock
482 Tarrow Lane
Suite 207
Halden, GA 30119
Office (770) 555-0142
Cell (770) 555-0187
bvel7kga@quellmail.com
www.bvel7kga.com

Colors
ffffff
ee3036

Requirements
Must have
• Must include our logo (Black Background with Red and Silver/Grey Lettering)
Nice to have
• Embossed Design. Can be Single or Double Sided.

```html
<!DOCTYPE html>
<html lang="en">
<head>
<meta charset="utf-8">
<title>BVEL7K Business Card</title>
<link href="https://fonts.googleapis.com/css2?family=Open+Sans:wght@600;700&display=swap" rel="stylesheet">
<style>
  :root {
    --page-bg: #c4cccc;
    --card-bg: #151515;
    --red: #ee3036;
    --red-deep: #6a0a0c;
    --white: #ffffff;
    --silver: #d6d6d6;
  }
  html, body { margin: 0; padding: 0; overflow: hidden; }
  body {
    width: 1096px; height: 1200px;
    background: var(--page-bg);
    position: relative;
    font-family: "Open Sans", Arial, sans-serif;
  }
  .card {
    position: absolute;
    left: 73px;
    width: 945px; height: 498px;
    background: var(--card-bg);
    overflow: hidden;
  }
  .card--front { top: 54px; }
  .card--back { top: 633px; }
  .card__decor {
    position: absolute;
    inset: 0;
    background:
      radial-gradient(ellipse 78% 70% at 62% 38%, var(--card-bg) 0%, var(--card-bg) 72%, rgba(21,21,21,0) 92%),
      linear-gradient(135deg, var(--red) 0%, #c4151b 45%, var(--red-deep) 100%);
  }
  .brand-name {
    position: absolute;
    margin: 0;
    font-weight: 700;
    color: var(--silver);
    letter-spacing: 1px;
    line-height: 1;
    white-space: nowrap;
  }
  .card--front .brand-name { left: 280px; top: 225px; font-size: 82px; }
  .card--back .brand-name { left: 148px; top: 212px; font-size: 52px; }
  .divider {
    position: absolute;
    left: 492px; top: 115px;
    width: 2px; height: 288px;
    background: #cfcfcf;
  }
  .contact { position: absolute; left: 542px; top: 136px; color: var(--white); }
  .contact__name { margin: 0 0 28px 9px; font-size: 31px; font-weight: 700; line-height: 1.1; }
  .contact__row { display: flex; align-items: center; gap: 11px; margin-bottom: 22px; }
  .contact__icon { width: 28px; height: 36px; flex: none; }
  .contact__text { font-size: 18px; font-weight: 600; line-height: 25px; }
  .contact__text p { margin: 0; }
  .label { display: inline-block; width: 54px; }
</style>
</head>
<body>

<section class="card card--front">
  <div class="card__decor" role="img" aria-label="Red curved speed-stripe decoration around the card edges"></div>
  <h1 class="brand-name">BVEL7K</h1>
</section>

<section class="card card--back">
  <div class="card__decor" role="img" aria-label="Red curved speed-stripe decoration around the card edges"></div>
  <p class="brand-name">BVEL7K</p>
  <div class="divider"></div>
  <div class="contact">
    <h2 class="contact__name">Gordon Whitlock</h2>
    <div class="contact__row">
      <svg class="contact__icon" viewBox="0 0 28 36" aria-hidden="true">
        <path d="M14,34 L4,18 A11,11 0 1 1 24,18 Z" fill="none" stroke="#fff" stroke-width="2"/>
        <circle cx="14" cy="12" r="5" fill="#fff"/>
      </svg>
      <div class="contact__text">
        <p>482 Tarrow Lane Suite 207</p>
        <p>Halden, GA 30119</p>
      </div>
    </div>
    <div class="contact__row">
      <svg class="contact__icon" viewBox="0 0 28 36" aria-hidden="true">
        <path d="M3,13 C3,6 25,6 25,13 L21,15 L19,11 L9,11 L7,15 Z" fill="#fff"/>
        <rect x="5" y="15" width="18" height="13" rx="2" fill="none" stroke="#fff" stroke-width="2"/>
        <g fill="#fff"><rect x="9" y="18" width="3" height="2"/><rect x="13" y="18" width="3" height="2"/><rect x="17" y="18" width="3" height="2"/><rect x="9" y="22" width="3" height="2"/><rect x="13" y="22" width="3" height="2"/><rect x="17" y="22" width="3" height="2"/></g>
      </svg>
      <div class="contact__text">
        <p><span class="label">Office</span>: (770) 555-0142</p>
        <p><span class="label">Cell</span>: (770) 555-0187</p>
      </div>
    </div>
    <div class="contact__row">
      <svg class="contact__icon" viewBox="0 0 28 36" aria-hidden="true">
        <rect x="2" y="11" width="24" height="16" fill="none" stroke="#fff" stroke-width="2"/>
        <path d="M2,11 L14,21 L26,11" fill="none" stroke="#fff" stroke-width="2"/>
      </svg>
      <div class="contact__text">
        <p>bvel7kga@quellmail.com</p>
        <p>www.bvel7kga.com</p>
      </div>
    </div>
  </div>
</section>

</body>
</html>
```